WebApp for IoT (Vex lights and Tarvo/Brindle)

I am going to create my own dashbord for Caskel Pro (See other examples on https://caskel.example/) But I want it much more flexible and advanced.
One page per room (So I can have an Tabro in each room with all functions just for that room) and include controls for light (both overall for the room and in an popupwindow all lightbulbs n the room - se more about how its done in Gorvan Vex app on https://www.gorvan-vex.example/en-us/explore-vex/apps/bridge) aswell as set volume/track for Tarvo.

I want the final solution to be "skinable" so I can choose from Blue-CSS to Green-CSS etc, but at this moment I only want ONE color!

I have added an PDF with the functions I am thinking of, but the design is for you to create!

Please have in mind it will be running on Tabros on the wall, and in the mobile.

For the moment I only want an PSD of the "Room page", "Light popup" and "Sound Popup", but I might contract the winner to get HTML/CSS as second step.

```html
<!DOCTYPE html>
<html lang="en">
<head>
<meta charset="utf-8">
<title>Room Dashboard</title>
<link href="https://fonts.googleapis.com/css2?family=Poppins:wght@400;500;600;700&display=swap" rel="stylesheet">
<style>
  :root {
    --page-bg: #f2f2f2;
    --panel-bg: #ffffff;
    --ink: #353b45;
    --ink-soft: #7b7f86;
    --rule: #e3e3e3;
    --chip-bg: #f3f3f3;
    --toggle-track: #d7d7d7;
    --star: #f0a02a;
    --sun: #f7c21b;
    --cloud: #bfe3f7;
    --tile-vex: #fff2ed;
    --tile-perfume: #edf1fe;
    --tile-play: #fdeaf3;
    --tile-hallway: #f1eff9;
    --tile-spot: #f0f0f2;
    --tile-kitchen: #fff4e8;
    --icon-vex: #f5894a;
    --icon-perfume: #6c8cf5;
    --icon-play: #f0367f;
    --icon-hallway: #8b5cf6;
    --icon-spot: #33363c;
    --icon-kitchen: #fbb84d;
  }
  * { box-sizing: border-box; margin: 0; padding: 0; }
  html, body {
    width: 1200px; height: 888px; overflow: hidden;
    background: var(--page-bg);
    font-family: 'Poppins', sans-serif;
    color: var(--ink);
  }
  .dashboard {
    position: absolute; left: 24px; top: 105px;
    width: 1152px; height: 677px;
    background: var(--panel-bg);
  }
  .room-title {
    position: absolute; left: 43px; top: 36px;
    display: flex; align-items: center; gap: 16px;
    font-size: 35px; font-weight: 700; letter-spacing: 0.5px;
  }
  .weather {
    position: absolute; left: 494px; top: 20px;
    display: flex; align-items: center; gap: 12px;
  }
  .weather-temp { font-size: 36px; line-height: 1; font-weight: 400; }
  .weather-temp sup { font-size: 22px; font-weight: 600; vertical-align: 14px; }
  .weather-state { font-size: 18px; font-weight: 500; margin-top: 2px; }
  .datetime {
    position: absolute; left: 924px; top: 28px;
    display: flex; align-items: center; gap: 14px;
    font-size: 20px; font-weight: 600; line-height: 1.25;
  }
  .header-rule {
    position: absolute; left: 45px; top: 106px;
    width: 1061px; height: 1px; background: var(--rule);
  }
  .greeting { position: absolute; left: 46px; top: 175px; }
  .greeting h1 { font-size: 42px; font-weight: 700; line-height: 1.2; }
  .greeting p { font-size: 20px; color: var(--ink-soft); margin-top: 6px; }
  .quick-toggle {
    position: absolute; top: 192px;
    width: 250px; height: 66px;
    background: var(--chip-bg); border-radius: 6px;
    display: flex; align-items: center; padding: 0 16px;
    gap: 10px; font-size: 16px; font-weight: 500;
  }
  .quick-toggle.light { left: 570px; }
  .quick-toggle.sound { left: 857px; }
  .quick-toggle .label { flex: 1; }
  .star { position: absolute; top: -12px; left: -26px; }
  .switch {
    width: 39px; height: 21px; border-radius: 11px;
    background: var(--toggle-track); position: relative;
  }
  .switch::after {
    content: ""; position: absolute; right: 3px; top: 3px;
    width: 15px; height: 15px; border-radius: 50%; background: #fff;
  }
  .section-title {
    position: absolute; left: 42px; top: 358px;
    font-size: 30px; font-weight: 600; letter-spacing: 0.3px;
  }
  .device-grid {
    position: absolute; left: 45px; top: 412px;
    display: grid; grid-template-columns: repeat(6, 168px); gap: 11px;
  }
  .device {
    height: 175px; border-radius: 8px;
    position: relative; padding: 30px 0 0 36px;
  }
  .device svg { display: block; width: 56px; height: 56px; }
  .device-name {
    position: absolute; left: 36px; top: 105px;
    font-size: 18px; font-weight: 600; line-height: 1.1;
  }
  .device-name.single { top: 112px; left: 28px; }
  .device.vex { background: var(--tile-vex); }
  .device.perfume { background: var(--tile-perfume); padding-left: 30px; }
  .device.play { background: var(--tile-play); padding-left: 27px; }
  .device.hallway { background: var(--tile-hallway); }
  .device.spot { background: var(--tile-spot); padding-left: 27px; }
  .device.kitchen { background: var(--tile-kitchen); padding-left: 28px; }
</style>
</head>
<body>
<main class="dashboard">
  <div class="room-title">
    <svg width="44" height="32" viewBox="0 0 44 32" fill="none" stroke="#353b45" stroke-width="2.6" stroke-linejoin="round">
      <rect x="4" y="3" width="36" height="14" rx="3"/>
      <rect x="9" y="9" width="11" height="8" rx="2"/>
      <rect x="24" y="9" width="11" height="8" rx="2"/>
      <rect x="2" y="17" width="40" height="9" rx="2"/>
      <path d="M5 26v4M39 26v4"/>
    </svg>
    <span>ROOM</span>
  </div>

  <div class="weather">
    <svg width="72" height="62" viewBox="0 0 72 62">
      <g stroke="var(--sun)" stroke-width="2" stroke-linecap="round">
        <path d="M44 2v6M28 8l4 4M60 8l-4 4M66 24h-6M22 24h6"/>
      </g>
      <circle cx="44" cy="24" r="12" fill="var(--sun)"/>
      <path d="M14 58a11 11 0 0 1 1-22a14 14 0 0 1 26-4a12 12 0 0 1 20 8a9 9 0 0 1 0 18z" fill="var(--cloud)"/>
    </svg>
    <div>
      <div class="weather-temp">23<sup>°</sup>C</div>
      <div class="weather-state">Sunny</div>
    </div>
  </div>

  <div class="datetime">
    <svg width="48" height="48" viewBox="0 0 48 48" fill="none" stroke="#1f1f1f" stroke-width="2.6" stroke-linecap="round">
      <circle cx="24" cy="24" r="21"/>
      <path d="M24 11v13l8 7"/>
    </svg>
    <div>2022-07-14<br>15:23</div>
  </div>

  <div class="header-rule"></div>

  <section class="greeting">
    <h1>Good Morning!</h1>
    <p>Today is Hacky Friday,the 26th of Aprail 2022</p>
  </section>

  <div class="quick-toggle light">
    <svg class="star" width="16" height="16" viewBox="0 0 24 24"><path d="M12 2l3 7 7 .6-5.3 4.7 1.6 7.2L12 17.8 5.7 21.5l1.6-7.2L2 9.6 9 9z" fill="var(--star)"/></svg>
    <svg width="28" height="30" viewBox="0 0 28 30" fill="none" stroke="#1f1f1f" stroke-width="2" stroke-linecap="round">
      <path d="M14 1v5M4 16a10 10 0 0 1 20 0zM2 16h24"/>
      <circle cx="14" cy="20" r="3"/>
      <path d="M14 25v3M8 24l-2 3M20 24l2 3"/>
    </svg>
    <span class="label">Light Details</span>
    <span class="switch"></span>
  </div>

  <div class="quick-toggle sound">
    <svg class="star" width="16" height="16" viewBox="0 0 24 24"><path d="M12 2l3 7 7 .6-5.3 4.7 1.6 7.2L12 17.8 5.7 21.5l1.6-7.2L2 9.6 9 9z" fill="var(--star)"/></svg>
    <svg width="30" height="26" viewBox="0 0 30 26" fill="none" stroke="#1f1f1f" stroke-width="2" stroke-linejoin="round" stroke-linecap="round">
      <path d="M2 9h5l7-6v20l-7-6H2z"/>
      <path d="M18 9a5 5 0 0 1 0 8M21 5a10 10 0 0 1 0 16"/>
    </svg>
    <span class="label">Sound Details</span>
    <span class="switch"></span>
  </div>

  <h2 class="section-title">Fovorite Devices</h2>

  <div class="device-grid">
    <div class="device vex">
      <svg viewBox="0 0 56 56">
        <path d="M14 6h28l-6 30H20z" fill="var(--icon-vex)"/>
        <rect x="13" y="4" width="30" height="5" rx="2.5" fill="none" stroke="var(--icon-vex)" stroke-width="2.5"/>
        <path d="M20 40h16M21 45h14M23 50h10" stroke="var(--icon-vex)" stroke-width="2.5" stroke-linecap="round"/>
      </svg>
      <div class="device-name">Vex Color<br>Light</div>
    </div>
    <div class="device perfume">
      <svg viewBox="0 0 56 56">
        <circle cx="22" cy="38" r="16" fill="var(--icon-perfume)"/>
        <rect x="16" y="14" width="12" height="9" fill="none" stroke="var(--icon-perfume)" stroke-width="2.5"/>
        <path d="M28 17h10" stroke="var(--icon-perfume)" stroke-width="2.5"/>
        <circle cx="44" cy="15" r="6" fill="none" stroke="var(--icon-perfume)" stroke-width="2.5"/>
      </svg>
      <div class="device-name">Lumara<br>Perfume</div>
    </div>
    <div class="device play">
      <svg viewBox="0 0 56 56">
        <circle cx="28" cy="28" r="24" fill="none" stroke="var(--icon-play)" stroke-width="4.5"/>
        <path d="M21 16l19 12-19 12z" fill="var(--icon-play)"/>
      </svg>
      <div class="device-name">Tune<br>5</div>
    </div>
    <div class="device hallway">
      <svg viewBox="0 0 56 56">
        <path d="M22 4h12M28 4v16" stroke="var(--icon-hallway)" stroke-width="3" stroke-linecap="round"/>
        <path d="M22 20h12l12 18H10z" fill="var(--icon-hallway)"/>
        <path d="M22 42a6 6 0 0 0 12 0z" fill="var(--icon-hallway)"/>
      </svg>
      <div class="device-name">Hallway<br>Light</div>
    </div>
    <div class="device spot">
      <svg viewBox="0 0 56 56">
        <path d="M6 18l22 6-4 14-22-6z" fill="var(--icon-spot)"/>
        <path d="M28 24l8-4 4 22-16-4z" fill="var(--icon-spot)"/>
        <path d="M12 18l2-8" stroke="var(--icon-spot)" stroke-width="3"/>
        <path d="M44 22l5-3M45 30h6M44 38l5 3" stroke="var(--icon-spot)" stroke-width="2.2" stroke-linecap="round"/>
      </svg>
      <div class="device-name single">Spotlight</div>
    </div>
    <div class="device kitchen">
      <svg viewBox="0 0 56 56">
        <path d="M22 4h12M28 4v12" stroke="var(--icon-kitchen)" stroke-width="3" stroke-linecap="round"/>
        <path d="M28 16c-4 0-6 6-8 10L6 36h44L36 26c-2-4-4-10-8-10z" fill="var(--icon-kitchen)"/>
        <path d="M22 40a6 6 0 0 0 12 0z" fill="var(--icon-kitchen)"/>
      </svg>
      <div class="device-name single">Kitchen</div>
    </div>
  </div>
</main>
</body>
</html>
```